The Corran & Wexby Irish Bar Bendigo

I need an app for my local hotel/pub. We have a bistro, functions and live entertainment every week. I would like to promote meal deals, drink offers, upcoming shows, members benefits. I would need to be able to update daily. Thanks
Updates

Reason: I am away on holidays until 19th July and can only get contact rarely so follow up is only on my phone not computer. Thanks Gordon

Target Market(s)

18+

Industry/Entity Type

Entertainment

Requirements
Must have
• Promotions
Entertainment
Functions
About the hotel

```html
<!DOCTYPE html>
<html lang="en">
<head>
<meta charset="utf-8">
<title>The Corran &amp; Wexby Irish Bar — Drinks Offers</title>
<link rel="stylesheet" href="https://fonts.googleapis.com/css2?family=Dosis:wght@500;600;700&family=Cabin:wght@400&family=Arimo:wght@400&display=swap">
<style>
  :root {
    --stage-light: #ffffff;
    --stage-dark: #b9b9b9;
    --header-top: #f4f6f7;
    --header-mid: #3a3d40;
    --header-bottom: #0d0e10;
    --body-top: #d6f4f5;
    --body-bottom: #b2e2e3;
    --nav-top: #e9eaee;
    --nav-bottom: #2a2d36;
    --strip: #121316;
    --offer-light: #ffc43a;
    --offer-dark: #f39a12;
    --panel: #f1f1f1;
    --accent-red: #c8102e;
    --copy-grey: #6b6b6b;
    --icon-white: #ffffff;
    --dot-orange: #f2a155;
    --social-grey: #8fa6b3;
    --note-ink: #111111;
    --arrow-grey: #8a8a8a;
  }
  * { margin: 0; padding: 0; box-sizing: border-box; }
  html, body { width: 1200px; height: 1169px; overflow: hidden; }
  body {
    position: relative;
    background: radial-gradient(ellipse 70% 75% at 62% 42%, var(--stage-light) 0%, #efefef 35%, var(--stage-dark) 100%);
    font-family: "Cabin", sans-serif;
  }
  .app-screen {
    position: absolute;
    left: 117px; top: 157px;
    width: 548px; height: 816px;
    box-shadow: 10px 10px 14px rgba(0,0,0,0.35);
  }
  .app-screen__chrome { position: absolute; inset: 0; }
  .screen-title {
    position: absolute;
    left: 0; top: 16px; width: 100%;
    text-align: center;
    font-family: "Dosis", sans-serif;
    font-weight: 600;
    font-size: 31px;
    letter-spacing: 1px;
    color: var(--icon-white);
    text-transform: uppercase;
  }
  .offer-photo {
    position: absolute;
    left: 36px; top: 105px;
    width: 290px; height: 396px;
    background: linear-gradient(150deg, #8e8f86 0%, #c9b7a7 25%, #e97a8a 45%, #6a6f6c 70%, #3c3f3e 100%);
    border: 2px solid #f4f4f4;
    box-shadow: 2px 3px 6px rgba(0,0,0,0.35);
  }
  .offer-badge {
    position: absolute;
    left: 274px; top: 111px;
    width: 196px; height: 196px;
    border-radius: 50%;
    background: radial-gradient(circle at 40% 35%, var(--offer-light) 0%, var(--offer-dark) 100%);
    border: 4px solid #fff6e0;
    box-shadow: 4px 6px 10px rgba(0,0,0,0.3);
    display: flex; align-items: center; justify-content: center;
    font-family: "Dosis", sans-serif;
    font-weight: 700;
    font-size: 56px;
    color: var(--icon-white);
  }
  .offer-details {
    position: absolute;
    left: 235px; top: 315px;
    width: 304px; height: 285px;
    background: var(--panel);
    padding: 14px 12px;
    box-shadow: 2px 3px 0 #9fd4d6;
  }
  .offer-details__heading {
    font-family: "Dosis", sans-serif;
    font-weight: 600;
    font-size: 22px;
    color: var(--accent-red);
    margin-bottom: 6px;
  }
  .offer-details__copy {
    font-size: 13.6px;
    line-height: 19.6px;
    color: var(--copy-grey);
  }
  .share-links {
    position: absolute;
    left: 180px; top: 622px;
    display: flex; gap: 12px;
  }
  .share-links__item {
    width: 47px; height: 47px;
    border-radius: 4px;
    background: var(--social-grey);
  }
  .design-notes {
    position: absolute;
    left: 23px; top: 1091px;
    font-family: "Arimo", sans-serif;
    font-size: 20.5px;
    color: var(--note-ink);
  }
  .note-arrows { position: absolute; inset: 0; pointer-events: none; }
</style>
</head>
<body>
  <section class="app-screen" aria-label="Drinks offers screen">
    <svg class="app-screen__chrome" width="548" height="816" viewBox="0 0 548 816">
      <defs>
        <linearGradient id="header-shade" x1="0" y1="0" x2="0" y2="1">
          <stop offset="0" stop-color="var(--header-top)"/>
          <stop offset="0.35" stop-color="var(--header-mid)"/>
          <stop offset="1" stop-color="var(--header-bottom)"/>
        </linearGradient>
        <linearGradient id="body-shade" x1="0" y1="0" x2="0" y2="1">
          <stop offset="0" stop-color="var(--body-top)"/>
          <stop offset="1" stop-color="var(--body-bottom)"/>
        </linearGradient>
        <linearGradient id="nav-shade" x1="0" y1="0" x2="0" y2="1">
          <stop offset="0" stop-color="var(--nav-top)"/>
          <stop offset="0.45" stop-color="#8d8f99"/>
          <stop offset="1" stop-color="var(--nav-bottom)"/>
        </linearGradient>
      </defs>
      <rect class="nav-bar" x="0" y="560" width="548" height="240" fill="url(#nav-shade)"/>
      <path class="content-area" d="M0 70 H548 V640 Q274 790 0 640 Z" fill="url(#body-shade)"/>
      <path class="content-edge" d="M0 640 Q274 790 548 640" fill="none" stroke="#ffffff" stroke-width="3" opacity="0.8"/>
      <rect class="header-bar" x="0" y="0" width="548" height="74" fill="url(#header-shade)"/>
      <polygon class="header-notch" points="262,74 284,74 273,85" fill="var(--header-bottom)"/>
      <rect class="base-strip" x="0" y="796" width="548" height="20" fill="var(--strip)"/>
      <g class="nav-icon nav-icon--meals" fill="var(--icon-white)">
        <rect x="44" y="716" width="4" height="20"/>
        <rect x="50" y="716" width="4" height="20"/>
        <rect x="56" y="716" width="4" height="20"/>
        <path d="M44 734 H60 V740 Q60 744 55 745 V764 H49 V745 Q44 744 44 740 Z"/>
        <path d="M66 716 Q76 722 76 740 V764 H70 V744 H66 Z"/>
      </g>
      <circle class="nav-dot" cx="104" cy="749" r="9" fill="var(--dot-orange)"/>
      <g class="nav-icon nav-icon--drinks" fill="var(--icon-white)">
        <circle cx="146" cy="739" r="6"/>
        <rect x="150" y="730" width="24" height="3" transform="rotate(-40 150 730)"/>
        <path d="M143 742 H175 L170 768 H148 Z"/>
      </g>
      <circle class="nav-dot" cx="216" cy="753" r="9" fill="var(--dot-orange)"/>
    </svg>
    <h1 class="screen-title">Drinks Offers</h1>
    <div class="offer-photo" role="img" aria-label="Photo of a cocktail glass at the bar"></div>
    <div class="offer-badge">OFFER</div>
    <article class="offer-details">
      <h2 class="offer-details__heading">DESCRIPTION</h2>
      <p class="offer-details__copy">Lorem ipsum dolor sit amet, consectetur adipiscing elit. Donec aliquet pulvinar semper. Suspendisse iaculis euismod augue, nec hendrerit est vehicula id. Lorem ipsum dolor sit amet, consectetur adipiscing elit. Lorem ipsum dolor sit amet, consectetur adipiscing elit.</p>
    </article>
    <nav class="share-links" aria-label="Share">
      <span class="share-links__item"></span>
      <span class="share-links__item"></span>
      <span class="share-links__item"></span>
    </nav>
  </section>

  <svg class="note-arrows" width="1200" height="1169" viewBox="0 0 1200 1169" fill="none" stroke="var(--arrow-grey)" stroke-width="2.5" stroke-linecap="round">
    <path d="M100 1082 Q108 1012 142 998"/>
    <path d="M128 994 L142 998 L134 1011"/>
    <path d="M210 1082 Q228 1020 268 992"/>
    <path d="M252 994 L268 992 L264 1007"/>
    <path d="M362 1078 Q420 1010 420 912"/>
    <path d="M532 1078 Q580 1000 542 912"/>
  </svg>
  <p class="design-notes">meal deals, drink offers, upcoming shows, members benefits.</p>
</body>
</html>
```